Professional Services/Construction Management (Millwork) Biz Cards

We've decided on a logo and have our color palette set, now we want to design some very professional looking cards that make a strong first impression - they'll reflect our tagline (that we're going to put on the back: Innovative. Professional. Leaders.

The example business card shows generally the direction we've been thinking of going for the back side - **but we're open to other ideas**

Target Market(s)

The cards should target more high-end (wealthy) owners and general contracting companies. We want them to convey a strong first impression - in a professional and not garish way.

Industry/Entity Type

Construction Company

Contact Information for Business Card

There needs to be a place for our company contractor's license number and business address. We want to also have people's names, titles, phone number, email address. The back can be the logo, tagline and web address

Requirements
Must have
• follow our color palette
Nice to have
• Font & Styles should compliment the Harrow Joinery fonts, but not necessarily match exactly

```html
<!DOCTYPE html>
<html lang="en">
<head>
<meta charset="utf-8">
<title>Harrow Joinery – Business Card</title>
<link rel="stylesheet" href="https://fonts.googleapis.com/css2?family=Cinzel:wght@500;600&family=Open+Sans:wght@300;400;700&display=swap">
<style>
  :root {
    --backdrop: #5a3420;
    --card-dark: #1b1b1b;
    --card-mid: #262626;
    --silver: #d9d9d9;
    --silver-soft: #a8a8a8;
    --rule: #bdbdbd;
    --emboss: #2f2f2f;
    --emboss-edge: #3a3a3a;
  }
  * { margin: 0; padding: 0; box-sizing: border-box; }
  html, body { width: 1200px; height: 1200px; overflow: hidden; }
  body {
    background: var(--backdrop);
    position: relative;
    font-family: "Open Sans", sans-serif;
    color: var(--silver);
  }
  .card {
    position: absolute;
    top: 134px;
    width: 514px;
    height: 854px;
    border-radius: 20px;
    overflow: hidden;
    background: radial-gradient(ellipse at 40% 30%, var(--card-mid), var(--card-dark) 75%);
    box-shadow: 0 6px 18px rgba(0,0,0,.45);
  }
  .card--back { left: 44px; }
  .card--front { left: 644px; }
  .card__curves { position: absolute; inset: 0; width: 100%; height: 100%; }

  .brand-mark {
    position: absolute;
    left: 118px; top: 206px;
    width: 296px; height: 296px;
    border-radius: 50%;
    border: 3px solid var(--silver);
    display: flex; align-items: center; justify-content: center;
  }
  .brand-mark__name {
    font-family: "Open Sans", sans-serif;
    font-weight: 700;
    font-size: 34px;
    letter-spacing: 2px;
    color: var(--silver);
    text-align: center;
    line-height: 1.1;
  }
  .brand-mark--faint { left: 106px; top: 38px; border: 2px solid var(--emboss-edge); }
  .brand-mark--faint .brand-mark__name { color: var(--emboss-edge); }

  .tagline {
    position: absolute;
    left: 0; width: 100%; top: 570px;
    text-align: center;
    font-family: "Cinzel", serif;
    font-weight: 600;
    font-size: 24px;
    line-height: 31px;
    letter-spacing: 1.5px;
    color: var(--silver);
    padding-left: 14px;
  }
  .rule {
    position: absolute;
    height: 2px;
    background: var(--rule);
    opacity: .85;
  }
  .website {
    position: absolute;
    left: 0; width: 100%; top: 788px;
    text-align: center;
    font-weight: 700;
    font-size: 19px;
    color: var(--silver-soft);
  }

  .license {
    position: absolute;
    left: 0; width: 100%; top: 366px;
    text-align: center;
    font-weight: 300;
    font-size: 14px;
    color: var(--silver-soft);
  }
  .person { position: absolute; left: 0; width: 100%; top: 538px; text-align: center; }
  .person__name { font-weight: 300; font-size: 40px; line-height: 50px; color: #f2f2f2; }
  .person__title { font-weight: 300; font-size: 29px; line-height: 30px; color: #f2f2f2; }
  .contact {
    position: absolute;
    left: 0; width: 100%; top: 652px;
    text-align: center;
    font-weight: 300;
    font-size: 20px;
    color: #ececec;
  }
  .contact__line { line-height: 30px; }
  .contact__line--tight { line-height: 23px; }
</style>
</head>
<body>

  <section class="card card--back" aria-label="Card back">
    <svg class="card__curves" viewBox="0 0 514 854" aria-hidden="true">
      <path d="M140 0 C 190 120, 260 250, 360 330" fill="none" stroke="#9a9a9a" stroke-width="3" opacity=".6"/>
      <path d="M290 0 C 300 90, 380 170, 514 200" fill="none" stroke="#0f0f0f" stroke-width="2" opacity=".8"/>
      <path d="M0 340 C 120 300, 300 330, 514 470" fill="none" stroke="#111" stroke-width="2" opacity=".6"/>
      <path d="M0 690 C 140 660, 300 700, 380 854" fill="none" stroke="#8a8a8a" stroke-width="2" opacity=".55"/>
      <path d="M300 640 C 380 700, 440 770, 470 854" fill="none" stroke="#111" stroke-width="2" opacity=".6"/>
    </svg>
    <div class="brand-mark">
      <span class="brand-mark__name">HARROW<br>Joinery</span>
    </div>
    <p class="tagline">Innovative<br>Professional<br>Leaders</p>
    <span class="rule" style="left:0; width:132px; top:614px;"></span>
    <span class="rule" style="left:388px; width:126px; top:616px;"></span>
    <p class="website">www.HarrowJoinery.com</p>
  </section>

  <section class="card card--front" aria-label="Card front">
    <svg class="card__curves" viewBox="0 0 514 854" aria-hidden="true">
      <path d="M170 420 C 300 460, 420 560, 514 640" fill="none" stroke="#111" stroke-width="2" opacity=".7"/>
      <path d="M180 460 C 300 520, 400 680, 440 854" fill="none" stroke="#111" stroke-width="2" opacity=".6"/>
      <path d="M0 660 C 100 680, 200 760, 250 854" fill="none" stroke="#111" stroke-width="2" opacity=".5"/>
      <path d="M300 560 C 380 620, 430 720, 460 854" fill="none" stroke="#333" stroke-width="1.5" opacity=".6"/>
    </svg>
    <div class="brand-mark brand-mark--faint">
      <span class="brand-mark__name">HARROW<br>Joinery</span>
    </div>
    <p class="license">license #&nbsp; 726104583</p>
    <div class="person">
      <p class="person__name">Martin Hale</p>
      <p class="person__title">ceo</p>
    </div>
    <span class="rule" style="left:4px; width:136px; top:567px;"></span>
    <span class="rule" style="left:386px; width:124px; top:565px;"></span>
    <div class="contact">
      <p class="contact__line">4180 Cedar Mill Road #212 Reno,</p>
      <p class="contact__line">NV 89502 United States</p>
      <p class="contact__line contact__line--tight">+1 775 555 0142 ext 118</p>
      <p class="contact__line contact__line--tight">martin@HarrowJoinery.com</p>
    </div>
  </section>

</body>
</html>
```